Hello,
We’re looking for a new WordPress website for Gather Your Light, our company offering unique well-being retreats and workshops.
We currently have a website online (you can consult it : www.gatheryourlight.ch), but we now need to build a new site on WordPress — more flexible, more intuitive to manage, and better aligned with our evolving needs.

What we’re looking for:
A new userfriendly WordPress site, with:
Inspiring, elegant, and modern design
Smooth user experience on desktop and mobile
Innovative design proposals – we want to be inspired !
SEO best practices
Respect of our existing color palette
The final website will need to be set up on our existing hosting provider (details can be shared later)

Pages to Include:
- Home
- Our Story
- Our Stays - with links to 5 individual pages, each describing one of our stays in detail.
- Activities – with potential links to individual descriptive pages
- Agenda
- Our Charter
- The Team
- Contact
- Blog

Required Features:
- Space for photos and videos
- Sections for testimonials and press articles
- Blog/article layout with strong readability
- Easy-to-update backend for future content
- Newsletter sign-up (pop-up and in footer)
- Additional pop-up on/off
- “Request info” buttons
- “Booking request” buttons
- Integration of our 4 pillars - Breathe · Feel · Connect · Experience - in the design (They’re currently in the footer, but we’re open to creative suggestions)

Who we are :
Gather Your Light offers well-being and personal growth stays but with a very different spirit.
We’re not a classic wellness brand. Our approach is professional, joyful, and grounded.
We create spaces where people can take a real break — breathe, slow down, and reconnect with themselves.
During our stays, people are welcomed like friends:
with warmth, respect, and no pressure.
Each program combines practices like breathwork, movement, creativity, coaching, and massages in a relaxed, beautiful setting of the French Alps.
What makes us different:
A friendly and down-to-earth atmosphere
A wide mix of activities.
A mix of inner work and simple pleasures
Private rooms, nourishing food, and shared moments
Time to talk, to laugh, to walk, or just be silent together - and feel free to be yourself
Our guests come to pause.
They leave feeling lighter, aligned, and full of life

```html
<!DOCTYPE html>
<html lang="en">
<head>
<meta charset="utf-8">
<title>Gather Your Light – Well-being Retreats</title>
<link href="https://fonts.googleapis.com/css2?family=Poppins:wght@400;500;600;700;800&family=Open+Sans:wght@400;600&display=swap" rel="stylesheet">
<style>
:root{
  --navy:#0b2660;
  --navy-deep:#07183f;
  --blue:#1d5bbf;
  --teal:#3aa9a3;
  --teal-dark:#1f7f86;
  --teal-light:#8fd3cd;
  --ice:#eaf2fb;
  --ink:#1d2535;
  --muted:#5d6676;
  --white:#ffffff;
  --line:#d7e3f1;
}
*{box-sizing:border-box;margin:0;padding:0}
html,body{width:1200px;height:4108px;overflow:hidden}
body{font-family:"Open Sans",sans-serif;color:var(--ink);background:var(--white);position:relative}
h1,h2,h3,h4,.btn,.nav,.brand{font-family:"Poppins",sans-serif}
.abs{position:absolute}
.ph{display:block}
.btn{display:inline-flex;align-items:center;gap:8px;height:34px;padding:0 18px;border-radius:20px;font-size:12px;font-weight:600;color:var(--white);background:var(--teal);border:none}
.btn.navy{background:var(--blue)}
.btn.outline{background:transparent;border:1.5px solid var(--white)}
.section-title{font-size:30px;font-weight:700;text-align:center;color:var(--ink);letter-spacing:.5px}

/* header + hero */
.hero{position:absolute;left:0;top:0;width:1200px;height:860px;overflow:hidden}
.hero-photo{position:absolute;inset:0;background:linear-gradient(90deg,#0a2458 0%,#15387a 38%,#7d9c6a 62%,#c7b88b 80%,#9fae7a 100%)}
.topbar{position:absolute;left:0;top:0;width:1200px;height:64px;display:flex;align-items:center;padding:0 40px;justify-content:space-between}
.brand{color:var(--white);font-weight:700;font-size:22px;letter-spacing:.5px;display:flex;align-items:center;gap:8px}
.brand .dot{width:10px;height:10px;border-radius:50%;background:var(--teal)}
.nav{display:flex;gap:22px;font-size:11px;font-weight:600;color:var(--white);align-items:center}
.nav .btn{height:28px;font-size:11px;background:var(--blue)}
.hero-copy{position:absolute;left:60px;top:150px;width:560px;color:var(--white)}
.hero-copy .eyebrow{display:inline-block;font-size:13px;padding:4px 10px;background:rgba(255,255,255,.12);border-radius:3px;margin-bottom:14px}
.hero-copy h1{font-size:50px;line-height:1.08;font-weight:800;letter-spacing:.5px}
.hero-copy h1 em{font-style:normal;color:var(--teal)}
.hero-copy p{font-size:13px;margin:16px 0 22px;opacity:.9;width:440px}
.hero-wave{position:absolute;left:0;top:690px}

/* pillars */
.pillars{position:absolute;left:0;top:700px;width:1200px;height:320px}
.pillar{position:absolute;top:20px;width:190px;height:190px;border-radius:50%;border:8px solid #e6f3f2;box-shadow:0 6px 18px rgba(30,80,120,.15)}
.pillar .ph{width:100%;height:100%;border-radius:50%;background:radial-gradient(circle at 50% 35%,#d9b9a0,#8fa5a2 60%,#5e7f86)}
.pillar span{position:absolute;left:0;right:0;top:72px;text-align:center;font-family:"Poppins",sans-serif;font-size:20px;font-weight:600;color:var(--white)}
.pillar .badge{position:absolute;left:62px;top:160px;width:50px;height:50px;border-radius:50%;background:var(--teal);border:4px solid var(--white);display:flex;align-items:center;justify-content:center}

/* about */
.about{position:absolute;left:0;top:1020px;width:1200px;height:470px;background:var(--ice)}
.about-photo{position:absolute;left:150px;top:70px;width:360px;height:360px;border-radius:50%;border:10px solid var(--white);box-shadow:0 0 0 3px var(--teal-light);background:radial-gradient(circle at 50% 40%,#e6d8c8,#a9b9a8 60%,#6f8b7f)}
.about-copy{position:absolute;left:560px;top:90px;width:520px}
.about-copy .eyebrow{font-size:11px;color:var(--muted)}
.about-copy h2{font-size:32px;font-weight:700;margin:4px 0 12px}
.about-copy p{font-size:12px;line-height:1.7;color:var(--muted);margin-bottom:18px}

/* stays */
.stays{position:absolute;left:0;top:1520px;width:1200px;height:470px}
.stays .section-title{position:absolute;left:0;right:0;top:30px}
.stay{position:absolute;top:90px;width:308px;height:300px;border-radius:10px;overflow:hidden;box-shadow:0 6px 18px rgba(20,40,80,.15);background:var(--white)}
.stay .ph{height:240px}
.stay .label{height:60px;display:flex;align-items:center;justify-content:space-between;padding:0 18px;font-family:"Poppins",sans-serif;font-weight:700;font-size:15px}
.arrow-dot{width:26px;height:26px;border-radius:50%;background:var(--teal);display:flex;align-items:center;justify-content:center}
.pager{position:absolute;left:0;right:0;display:flex;justify-content:center;align-items:center;gap:12px}
.pager .circ{width:26px;height:26px;border-radius:50%;border:1.5px solid var(--line);display:flex;align-items:center;justify-content:center}

/* testimonial */
.testimonial{position:absolute;left:0;top:2020px;width:1200px;height:340px;background:linear-gradient(180deg,#2e9fa0,#1c6e88 60%,#0f3d6f);overflow:hidden}
.testimonial h2{position:absolute;left:0;right:0;top:28px;text-align:center;color:var(--white);font-size:28px;font-weight:700}
.quote{position:absolute;left:200px;top:100px;width:800px;color:var(--white)}
.quote .mark{font-family:"Poppins",sans-serif;font-size:54px;line-height:1;font-weight:700}
.quote p{font-size:14px;line-height:1.65;margin-top:-10px}
.quote .who{text-align:right;margin-top:12px;font-family:"Poppins",sans-serif;font-weight:600;font-size:13px}

/* activities */
.activities{position:absolute;left:0;top:2380px;width:1200px;height:620px}
.activities .section-title{position:absolute;left:0;right:0;top:20px}
.act-hub{position:absolute;left:430px;top:110px;width:340px;height:340px;border-radius:50%;border:2px solid var(--teal-light)}
.act-photo{position:absolute;left:470px;top:150px;width:260px;height:260px;border-radius:50%;background:radial-gradient(circle at 50% 40%,#f1e0d3,#c6b29f 55%,#7d8e95)}
.act-node{position:absolute;width:44px;height:44px;border-radius:50%;background:var(--teal);display:flex;align-items:center;justify-content:center;border:4px solid var(--white);box-shadow:0 0 0 2px var(--teal-light)}
.act{position:absolute;width:300px}
.act h3{font-size:14px;font-weight:700;margin-bottom:4px}
.act p{font-size:11px;line-height:1.5;color:var(--muted)}
.act.left{text-align:right}
.watermark{position:absolute;left:0;right:0;top:560px;text-align:center;font-family:"Poppins",sans-serif;font-size:78px;font-weight:800;letter-spacing:6px;color:#eef2f7}

/* cta */
.cta{position:absolute;left:0;top:3020px;width:1200px;height:260px;background:linear-gradient(90deg,#0b3a4a 0%,#0f4d5a 45%,#2b6e64 75%,#4d7c5c 100%);color:var(--white)}
.cta-inner{position:absolute;left:0;right:0;top:70px;text-align:center}
.cta h2{font-size:34px;font-weight:700}
.cta p{font-size:13px;margin:6px 0 20px;opacity:.9}

/* blog */
.blog{position:absolute;left:0;top:3300px;width:1200px;height:480px}
.blog .section-title{position:absolute;left:0;right:0;top:10px}
.post{position:absolute;top:70px;width:308px;height:300px;border-radius:10px;overflow:hidden;background:var(--white);box-shadow:0 6px 18px rgba(20,40,80,.15)}
.post .ph{height:190px}
.post .date{position:absolute;left:12px;top:12px;background:var(--blue);color:var(--white);font-size:10px;font-weight:600;padding:3px 8px;border-radius:3px;font-family:"Poppins",sans-serif}
.post .body{padding:14px 16px;position:relative}
.post h3{font-size:15px;font-weight:700;color:var(--teal-dark)}
.post p{font-size:11px;color:var(--muted);margin-top:6px;width:230px;line-height:1.5}
.post .arrow-dot{position:absolute;right:16px;top:40px}

/* footer */
.footer{position:absolute;left:0;top:3790px;width:1200px;height:318px;background:var(--navy-deep);color:#c6d0e2}
.footer-wave{position:absolute;left:0;top:-20px}
.fcol{position:absolute;top:50px;font-size:11px;line-height:2}
.fcol h4{font-size:12px;color:var(--white);font-weight:600;margin-bottom:6px}
.fcol .item{display:flex;align-items:center;gap:8px}
.fcol .sq{width:22px;height:22px;border-radius:50%;background:#1b356b;flex:none}
.news-input{width:170px;height:30px;border-radius:15px;background:var(--white);margin:8px 0;padding:0 12px;font-size:10px;color:var(--muted);display:flex;align-items:center}
.copyright{position:absolute;left:0;right:0;bottom:0;height:40px;border-top:1px solid #1d2f5a;display:flex;align-items:center;justify-content:center;font-size:11px}
</style>
</head>
<body>

<!-- HERO -->
<section class="hero">
  <div class="hero-photo ph" role="img" aria-label="Young woman smiling and blowing a dandelion in a sunlit meadow"></div>
  <header class="topbar">
    <div class="brand"><span class="dot"></span>Gather Your Light</div>
    <nav class="nav">
      <span>OUR STORY</span><span>OUR STAYS</span><span>ACTIVITIES</span><span>AGENDA</span><span>OUR CHARTER</span><span>THE TEAM</span><span>BLOG</span><span>CONTACT</span>
      <span class="btn">Request Info</span>
    </nav>
  </header>
  <div class="hero-copy">
    <span class="eyebrow">Welcome to Gather Your Light</span>
    <h1>WHERE <em>BREATH</em> MEETS<br>STILLNESS AND JOY.</h1>
    <p>Welcoming retreats in the French Alps for people ready to slow down, reconnect and feel more alive.</p>
    <span class="btn">Explore Our Stays</span>
    <span class="btn navy" style="margin-left:10px">Booking Request</span>
  </div>
  <svg class="hero-wave" width="1200" height="170" viewBox="0 0 1200 170">
    <path d="M0 40 Q600 170 1200 20 L1200 170 L0 170Z" fill="#ffffff"/>
    <path d="M0 40 Q600 170 1200 20" fill="none" stroke="#1d5bbf" stroke-width="6"/>
    <path d="M0 56 Q600 180 1200 36" fill="none" stroke="#3aa9a3" stroke-width="2"/>
  </svg>
</section>

<!-- PILLARS -->
<section class="pillars">
  <div class="pillar" style="left:135px"><div class="ph" role="img" aria-label="Guest breathing deeply outdoors"></div><span>Breath</span>
    <div class="badge"><svg width="22" height="22" viewBox="0 0 24 24" fill="none" stroke="#fff" stroke-width="2"><path d="M3 9h11a3 3 0 1 0-3-3M3 15h15a3 3 0 1 1-3 3"/></svg></div></div>
  <div class="pillar" style="left:375px"><div class="ph" role="img" aria-label="Guest relaxing with eyes closed"></div><span>Feel</span>
    <div class="badge"><svg width="22" height="22" viewBox="0 0 24 24" fill="none" stroke="#fff" stroke-width="2"><path d="M12 20s-7-4.5-7-10a4 4 0 0 1 7-2.5A4 4 0 0 1 19 10c0 5.5-7 10-7 10z"/></svg></div></div>
  <div class="pillar" style="left:615px"><div class="ph" role="img" aria-label="Guests sharing a warm moment together"></div><span>Connect</span>
    <div class="badge"><svg width="22" height="22" viewBox="0 0 24 24" fill="none" stroke="#fff" stroke-width="2"><circle cx="8" cy="9" r="3"/><circle cx="16" cy="9" r="3"/><path d="M3 19c1-3 3-4 5-4s4 1 5 4M11 19c1-3 3-4 5-4s4 1 5 4"/></svg></div></div>
  <div class="pillar" style="left:855px"><div class="ph" role="img" aria-label="Guest enjoying a mountain experience"></div><span>Experience</span>
    <div class="badge"><svg width="22" height="22" viewBox="0 0 24 24" fill="none" stroke="#fff" stroke-width="2"><path d="M3 19l6-10 4 6 3-4 5 8z"/></svg></div></div>
</section>

<!-- ABOUT -->
<section class="about">
  <div class="about-photo ph" role="img" aria-label="Woman meditating cross-legged in a bright room"></div>
  <div class="about-copy">
    <span class="eyebrow">Get to know us</span>
    <h2>ABOUT GATHER YOUR LIGHT</h2>
    <p>Gather Your Light was born from a simple wish: to create a place where people can truly pause. Our stays blend breathwork, movement, creativity, coaching and massage in the calm of the French Alps. We welcome every guest like a friend, with warmth, respect and no pressure at all. Private rooms, nourishing food and shared moments give space to talk, to laugh, to walk or simply to be silent together.</p>
    <p>We are not a classic wellness brand. Our approach is professional, joyful and grounded, so you can leave feeling lighter, aligned and full of life.</p>
    <span class="btn">Read Our Story <svg width="10" height="10" viewBox="0 0 10 10"><path d="M2 5h6M5 2l3 3-3 3" stroke="#fff" fill="none" stroke-width="1.5"/></svg></span>
  </div>
</section>

<!-- STAYS -->
<section class="stays">
  <h2 class="section-title">OUR STAYS</h2>
  <div class="stay" style="left:120px"><div class="ph" role="img" aria-label="Group seated in a circle during a workshop" style="background:linear-gradient(135deg,#c9b49b,#7f8f8a 60%,#4d5f6a)"></div>
    <div class="label">INSTANT WORKSHOPS<span class="arrow-dot"><svg width="10" height="10" viewBox="0 0 10 10"><path d="M2 5h6M5 2l3 3-3 3" stroke="#fff" fill="none" stroke-width="1.5"/></svg></span></div></div>
  <div class="stay" style="left:446px"><div class="ph" role="img" aria-label="Lit tent under a starry night sky" style="background:linear-gradient(180deg,#1a2a52,#3b4a7a 55%,#d08a3c 85%,#2f2a2a)"></div>
    <div class="label">4-NIGHT GETAWAY<span class="arrow-dot"><svg width="10" height="10" viewBox="0 0 10 10"><path d="M2 5h6M5 2l3 3-3 3" stroke="#fff" fill="none" stroke-width="1.5"/></svg></span></div></div>
  <div class="stay" style="left:772px"><div class="ph" role="img" aria-label="Airplane flying over a sunset horizon" style="background:linear-gradient(180deg,#243c78,#5a6fa8 50%,#e39a6a 85%,#2b2b3f)"></div>
    <div class="label">6-NIGHT FLIGHT<span class="arrow-dot"><svg width="10" height="10" viewBox="0 0 10 10"><path d="M2 5h6M5 2l3 3-3 3" stroke="#fff" fill="none" stroke-width="1.5"/></svg></span></div></div>
  <div class="pager" style="top:422px">
    <span class="circ"><svg width="10" height="10" viewBox="0 0 10 10"><path d="M6 2L3 5l3 3" stroke="#5d6676" fill="none" stroke-width="1.5"/></svg></span>
    <span class="btn navy">View All Retreats</span>
    <span class="circ"><svg width="10" height="10" viewBox="0 0 10 10"><path d="M4 2l3 3-3 3" stroke="#5d6676" fill="none" stroke-width="1.5"/></svg></span>
  </div>
</section>

<!-- TESTIMONIAL -->
<section class="testimonial">
  <svg class="abs" style="left:0;top:0" width="1200" height="340" viewBox="0 0 1200 340">
    <path d="M0 250 Q300 200 600 260 T1200 230 L1200 340 L0 340Z" fill="rgba(255,255,255,.06)"/>
    <path d="M0 290 Q400 240 800 300 T1200 280" fill="none" stroke="rgba(255,255,255,.25)" stroke-width="2"/>
    <path d="M60 170l-14 12 14 12" fill="none" stroke="#fff" stroke-width="2"/>
    <path d="M1140 170l14 12-14 12" fill="none" stroke="#fff" stroke-width="2"/>
  </svg>
  <h2>TESTIMONIAL</h2>
  <div class="quote">
    <div class="mark">&ldquo;</div>
    <p>What surprised me the most was how deeply connected I felt, not only to the other participants but to myself. This mix of breathwork, movement, creativity and conversation opened something in me I had forgotten was there. This wasn't just a retreat, it was a return. And the quiet joy I found there is something I now carry with me every day.</p>
    <div class="who">— LENA M. HARTWELL</div>
  </div>
</section>

<!-- ACTIVITIES -->
<section class="activities">
  <div class="watermark">GATHER YOUR LIGHT</div>
  <h2 class="section-title">ACTIVITIES</h2>
  <div class="act-hub"></div>
  <div class="act-photo ph" role="img" aria-label="Woman in prayer pose meditating"></div>

  <div class="act-node" style="left:478px;top:138px"><svg width="18" height="18" viewBox="0 0 24 24" fill="none" stroke="#fff" stroke-width="2"><path d="M3 9h11a3 3 0 1 0-3-3M3 15h15a3 3 0 1 1-3 3"/></svg></div>
  <div class="act-node" style="left:678px;top:138px"><svg width="18" height="18" viewBox="0 0 24 24" fill="none" stroke="#fff" stroke-width="2"><path d="M12 3v18M6 9l6-6 6 6"/></svg></div>
  <div class="act-node" style="left:408px;top:258px"><svg width="18" height="18" viewBox="0 0 24 24" fill="none" stroke="#fff" stroke-width="2"><circle cx="12" cy="12" r="8"/><circle cx="12" cy="12" r="2"/></svg></div>
  <div class="act-node" style="left:748px;top:258px"><svg width="18" height="18" viewBox="0 0 24 24" fill="none" stroke="#fff" stroke-width="2"><path d="M12 3v18M3 12h18M6 6l12 12M18 6L6 18"/></svg></div>
  <div class="act-node" style="left:478px;top:380px"><svg width="18" height="18" viewBox="0 0 24 24" fill="none" stroke="#fff" stroke-width="2"><circle cx="12" cy="5" r="2"/><path d="M12 8v7M7 11h10M9 21l3-6 3 6"/></svg></div>
  <div class="act-node" style="left:678px;top:380px"><svg width="18" height="18" viewBox="0 0 24 24" fill="none" stroke="#fff" stroke-width="2"><path d="M5 14c3 0 4-3 7-3s4 3 7 3M5 18c3 0 4-3 7-3s4 3 7 3"/></svg></div>

  <div class="act left" style="left:150px;top:130px"><h3>BREATHWORK</h3><p>Guided sessions to calm the nervous system and return to the present moment.</p></div>
  <div class="act" style="left:750px;top:130px"><h3>TIME IN NATURE</h3><p>Walks in the Alpine meadows and quiet moments to slow down, reflect and breathe.</p></div>
  <div class="act left" style="left:90px;top:258px"><h3>CREATIVITY &amp; EXPRESSION</h3><p>Painting, writing and playful workshops to let your inner voice speak freely.</p></div>
  <div class="act" style="left:810px;top:258px"><h3>CIRCLE TIME &amp; COACHING</h3><p>Open, respectful circles and coaching to reflect, share and feel supported.</p></div>
  <div class="act left" style="left:150px;top:380px"><h3>MOVEMENT &amp; BODYWORK</h3><p>Gentle yoga, dance and body awareness to help you feel at home in your body.</p></div>
  <div class="act" style="left:750px;top:380px"><h3>MASSAGE &amp; TOUCH THERAPY</h3><p>Deep, restorative massages that release tension and restore your energy.</p></div>

  <div class="pager" style="top:500px"><span class="btn navy">Explore All Activities</span></div>
</section>

<!-- CTA -->
<section class="cta">
  <div class="ph abs" role="img" aria-label="Misty alpine landscape at dusk" style="inset:0;background:linear-gradient(180deg,rgba(255,255,255,.04),rgba(0,0,0,.25))"></div>
  <div class="cta-inner">
    <h2>READY TO GATHER YOUR LIGHT?</h2>
    <p>Take a real pause. Reconnect with yourself. Join us in the French Alps for an experience that stays with you.</p>
    <span class="btn">Explore Our Stays</span>
    <span class="btn outline" style="margin-left:10px">Book now</span>
  </div>
</section>

<!-- BLOG -->
<section class="blog">
  <h2 class="section-title">BLOG</h2>
  <article class="post" style="left:120px"><div class="ph" role="img" aria-label="Cosy bedroom with white linen" style="background:linear-gradient(135deg,#e9e3da,#b9ab98 60%,#7f7466)"></div>
    <span class="date">APRIL 2025</span>
    <div class="body"><h3>ESCAPE :</h3><p>From Friday, April 18 to Monday, April 21 · Four days to unwind</p>
      <span class="arrow-dot"><svg width="10" height="10" viewBox="0 0 10 10"><path d="M2 5h6M5 2l3 3-3 3" stroke="#fff" fill="none" stroke-width="1.5"/></svg></span></div></article>
  <article class="post" style="left:446px"><div class="ph" role="img" aria-label="Colourful plated dish with flowers" style="background:linear-gradient(135deg,#f2efe6,#d9b25a 45%,#7a9a5a 75%,#4a4a3a)"></div>
    <span class="date">JUNE 2025</span>
    <div class="body"><h3>PARENTHESE :</h3><p>From Friday, June 27 to Sunday, June 29 · A short summer break</p>
      <span class="arrow-dot"><svg width="10" height="10" viewBox="0 0 10 10"><path d="M2 5h6M5 2l3 3-3 3" stroke="#fff" fill="none" stroke-width="1.5"/></svg></span></div></article>
  <article class="post" style="left:772px"><div class="ph" role="img" aria-label="Bright living room with mountain view" style="background:linear-gradient(135deg,#dfe8ee,#a9bccb 55%,#5f7888)"></div>
    <span class="date">JULY 2025</span>
    <div class="body"><h3>FLIGHT :</h3><p>From Sunday, July 13 to Saturday, July 19 · Six nights to breathe</p>
      <span class="arrow-dot"><svg width="10" height="10" viewBox="0 0 10 10"><path d="M2 5h6M5 2l3 3-3 3" stroke="#fff" fill="none" stroke-width="1.5"/></svg></span></div></article>
  <div class="pager" style="top:402px">
    <span class="circ"><svg width="10" height="10" viewBox="0 0 10 10"><path d="M6 2L3 5l3 3" stroke="#5d6676" fill="none" stroke-width="1.5"/></svg></span>
    <span class="btn navy">View All Blog</span>
    <span class="circ"><svg width="10" height="10" viewBox="0 0 10 10"><path d="M4 2l3 3-3 3" stroke="#5d6676" fill="none" stroke-width="1.5"/></svg></span>
  </div>
</section>

<!-- FOOTER -->
<footer class="footer">
  <svg class="footer-wave" width="1200" height="40" viewBox="0 0 1200 40"><path d="M0 40 Q600 0 1200 30 L1200 40Z" fill="#07183f"/><path d="M0 38 Q600 -2 1200 28" fill="none" stroke="#1d5bbf" stroke-width="3"/></svg>
  <div class="fcol" style="left:60px;width:240px">
    <div class="brand" style="font-size:20px;margin-bottom:10px"><span class="dot"></span>Gather Your Light</div>
    <p style="line-height:1.7">Gather Your Light offers well-being and personal growth stays with a very different spirit. We're a joyful, grounded team welcoming you like friends in the French Alps.</p>
  </div>
  <div class="fcol" style="left:360px">
    <h4>QUICK LINK</h4>
    <div>Our Story</div><div>Our Stays</div><div>Activities</div><div>Agenda</div><div>Our Charter</div><div>The Team</div><div>Blog</div><div>Contact</div>
  </div>
  <div class="fcol" style="left:470px;width:220px">
    <h4>CONTACT US</h4>
    <div class="item"><span class="sq"></span>12 Rue des Alpes, 74400 Chamonix</div>
    <div class="item"><span class="sq"></span>+41 22 555 01 47</div>
    <div class="item"><span class="sq"></span>hello@gatheryourlight.ch</div>
    <div class="item"><span class="sq"></span>www.gatheryourlight.ch</div>
  </div>
  <div class="fcol" style="left:740px">
    <h4>COMMUNITY</h4>
    <div class="item"><span class="sq"></span>Community</div>
    <div class="item"><span class="sq"></span>Photo stories</div>
    <div class="item"><span class="sq"></span>Videos</div>
  </div>
  <div class="fcol" style="left:920px;width:220px">
    <h4>NEWSLETTER</h4>
    <div style="line-height:1.5">Subscribe to our Newsletter</div>
    <div class="news-input">Enter your email</div>
    <span class="btn" style="height:28px">Subscribe <svg width="10" height="10" viewBox="0 0 10 10"><path d="M2 5h6M5 2l3 3-3 3" stroke="#fff" fill="none" stroke-width="1.5"/></svg></span>
  </div>
  <div class="copyright">© 2025 Gather Your Light. All rights reserved.</div>
</footer>

</body>
</html>
```